Business Promotion A1 Poster

I need an A1 poster for a lift in my building. It needs to promote BrightHarbour aa an employment expert for small business wanting to get their employment stuff right. We do on-site employment audits in Wellington for free.

We help small business manage the new 90 day trial period and help them design office/business policy manuals to avoid workplace problems.

The final design needs to convey expert and experience in employment. We use orange and grey as corporate colours. The company logo can be found on our website www.brightharbour.co.nz

Target Market(s)

Small business owners and managers

Industry/Entity Type

Small Business

Requirements
Nice to have
• colour information experts employment law in NZ

```html
<!DOCTYPE html>
<html lang="en">
<head>
<meta charset="utf-8">
<title>BrightHarbour – Empowering employers</title>
<link rel="stylesheet" href="https://fonts.googleapis.com/css2?family=Arimo:wght@400;700&display=swap">
<style>
  :root {
    --orange: #f39332;
    --orange-deep: #ee8a2a;
    --grey-text: #9a9a9a;
    --grey-light: #b5b5b5;
    --white: #ffffff;
    --photo-dark: #4a4a4c;
    --photo-mid: #a9a9ab;
    --photo-light: #e9e9ea;
  }
  * { margin: 0; padding: 0; box-sizing: border-box; }
  html, body { width: 849px; height: 1200px; overflow: hidden; background: var(--white); }
  body { font-family: "Arimo", Arial, sans-serif; }

  .poster { position: relative; width: 849px; height: 1200px; overflow: hidden; background: var(--white); }

  .hero-visual {
    position: absolute; left: 0; top: 0; width: 849px; height: 620px;
    background:
      radial-gradient(ellipse 320px 260px at 270px 180px, #d8cbbd 0%, rgba(216,203,189,0) 70%),
      radial-gradient(ellipse 300px 120px at 520px 520px, rgba(90,70,50,0.55) 0%, rgba(90,70,50,0) 70%),
      linear-gradient(160deg, var(--photo-dark) 0%, var(--photo-mid) 28%, var(--photo-light) 55%, #c9c9cb 78%, #8d8d8f 100%);
  }

  .headline {
    position: absolute; left: 66px; top: 412px;
    color: var(--orange); font-weight: 700; font-size: 106px;
    line-height: 88px; letter-spacing: -4px;
  }

  .offer-band {
    position: absolute; left: 0; top: 620px; width: 849px; height: 358px;
    background: var(--orange);
  }
  .services {
    position: absolute; left: 72px; top: 44px; list-style: none;
    color: var(--white); font-size: 24.5px; line-height: 33px;
  }
  .services li { position: relative; padding-left: 26px; }
  .services li::before {
    content: ""; position: absolute; left: 1px; top: 13px;
    width: 9px; height: 9px; border-radius: 50%; background: var(--white);
  }
  .expertise { position: absolute; left: 70px; top: 248px; color: var(--white); }
  .expertise-title { font-size: 34px; font-weight: 700; line-height: 40px; }
  .expertise-sub { font-size: 24.5px; line-height: 32px; }

  .brand-box {
    position: absolute; left: 527px; top: 252px; width: 236px; height: 106px;
    background: var(--white);
    display: flex; align-items: center; justify-content: center; gap: 12px;
  }
  .brand-name { color: var(--grey-text); font-size: 27px; font-weight: 400; }
  .brand-square { width: 26px; height: 26px; background: var(--orange); }

  .contact { position: absolute; right: 86px; top: 1006px; text-align: right; }
  .contact-call { color: var(--grey-light); font-size: 34px; line-height: 42px; }
  .contact-phone { color: var(--orange); font-size: 45px; line-height: 50px; }
  .contact-web { color: var(--grey-light); font-size: 32px; line-height: 40px; margin-top: 4px; }
  .contact-address { color: var(--grey-light); font-size: 16.5px; line-height: 20px; }
</style>
</head>
<body>
<main class="poster">
  <div class="hero-visual" role="img" aria-label="Photograph of a brushed metal jigsaw puzzle piece lifting above a grey surface, casting a long shadow"></div>

  <h1 class="headline">Empowering<br>employers</h1>

  <section class="offer-band">
    <ul class="services">
      <li>help you get the employment stuff right</li>
      <li>help you get the right person for the job</li>
      <li>help you get the policies not the problems</li>
      <li>help you manage the 90 day trial period</li>
      <li>help you re-structure your business</li>
    </ul>
    <div class="expertise">
      <p class="expertise-title">Experts</p>
      <p class="expertise-sub">in employment and recruitment</p>
    </div>
    <div class="brand-box">
      <span class="brand-name">BrightHarbour</span>
      <span class="brand-square"></span>
    </div>
  </section>

  <footer class="contact">
    <p class="contact-call">Call us today</p>
    <p class="contact-phone">+64 4 555 0142</p>
    <p class="contact-web">www.brightharbour.co.nz</p>
    <p class="contact-address">Level 5 / Harbourview Chambers, 14 Quay Lane</p>
  </footer>
</main>
</body>
</html>
```